Payroll Brochure

Create a brochure with the copy i have provided . A simple easy tp read brochure that shows wat we do we handle payroll taxes insurance 401k etc

```html
<!DOCTYPE html>
<html lang="en">
<head>
<meta charset="utf-8">
<title>Payroll Services Brochure – Inside Spread</title>
<link rel="stylesheet" href="https://fonts.googleapis.com/css2?family=EB+Garamond:wght@400;600;700&display=swap">
<style>
  :root {
    --paper: #f1f2f4;
    --maroon: #4f111b;
    --gold: #f0c400;
    --ink: #2a2a2a;
    --photo-dark: #3c3c3c;
    --photo-light: #c9c9c9;
  }
  * { margin: 0; padding: 0; box-sizing: border-box; }
  html, body { width: 1200px; height: 849px; overflow: hidden; background: var(--paper); }
  .spread {
    position: relative; width: 1200px; height: 849px; overflow: hidden;
    background: var(--paper);
    font-family: "EB Garamond", Garamond, serif;
    color: var(--ink);
  }
  .backdrop { position: absolute; inset: 0; width: 1200px; height: 849px; }
  .section { position: absolute; }
  .section::before {
    content: ""; display: block; width: 85px; height: 6px; background: var(--gold);
  }
  .section-title {
    font-size: 17px; font-weight: 600; color: var(--maroon);
    line-height: 18px; margin-top: 12px; letter-spacing: -0.1px;
  }
  .section-intro { font-size: 12.4px; line-height: 14.1px; margin-bottom: 14px; }
  .feature { font-size: 12.4px; line-height: 14.1px; margin-left: 36px; margin-bottom: 14.1px; }
  .feature:last-child { margin-bottom: 0; }
  .feature strong { font-weight: 700; color: #1c1c1c; }
  .col-left { left: 172px; }
  .col-left .feature { width: 360px; }
  .col-left .section-intro { width: 396px; }
  .col-right { left: 636px; }
  .col-right .feature { width: 400px; }
  .col-right .section-intro { width: 436px; }
</style>
</head>
<body>
<div class="spread">
  <svg class="backdrop" viewBox="0 0 2296 1624" preserveAspectRatio="none" aria-hidden="false">
    <defs>
      <linearGradient id="towerTone" x1="0" y1="0" x2="1" y2="1">
        <stop offset="0" stop-color="#9a9a9a"/>
        <stop offset="0.5" stop-color="var(--photo-dark)"/>
        <stop offset="1" stop-color="#5a5a5a"/>
      </linearGradient>
      <linearGradient id="meetingTone" x1="0" y1="0" x2="1" y2="0">
        <stop offset="0" stop-color="#d8d8d8"/>
        <stop offset="0.6" stop-color="#8a8a8a"/>
        <stop offset="1" stop-color="#bdbdbd"/>
      </linearGradient>
    </defs>
    <g role="img" aria-label="Black and white photo of a glass office tower seen from below">
      <polygon points="0,200 133,195 325,300 325,1165 0,980" fill="url(#towerTone)"/>
    </g>
    <polygon points="0,75 133,153 133,277 0,200" fill="var(--maroon)"/>
    <polygon points="0,980 325,1165 325,1292 0,1102" fill="var(--maroon)"/>
    <polygon points="0,1102 325,1292 325,1624 0,1624" fill="var(--gold)"/>
    <g role="img" aria-label="Black and white photo of colleagues in a meeting at a table with laptops">
      <polygon points="1640,0 2296,0 2296,470 1760,160 1760,60" fill="url(#meetingTone)"/>
    </g>
    <polygon points="1445,0 1640,0 1760,60 1760,185" fill="var(--maroon)"/>
  </svg>

  <section class="section col-left" style="top:61px">
    <h2 class="section-title">Payroll</h2>
    <p class="feature"><strong>Flexible</strong> - Halvern’S flexible and powerful payroll module allows you the ability to grow you’re your business by meeting your unique needs. Supporting payrolls for very large to very small companies,</p>
    <p class="feature"><strong>Efficient</strong> -&nbsp; Get payroll done efficiently and accurately by relying on our flexible design to handle even the most complex payroll needs.</p>
    <p class="feature"><strong>Grow without Growing Pains</strong> - Halvern’S technology and design is able to allow you to scale your business without adding all the incremental costs typically required.</p>
  </section>

  <section class="section col-left" style="top:263px">
    <h2 class="section-title">Tax Reporting &amp; Payments</h2>
    <p class="feature"><strong>Accurate</strong> - All payroll taxes (federal, state, local) are calculated accurately. Additionally, we determine proper local tax jurisdictions based on the employee home and work addresses.</p>
    <p class="feature"><strong>Complete</strong> - Federal, State, and Local withholding taxes as well as State and Federal Unemployment taxes are prepared. Tax payments are integrated into the Accounts Payable and General Ledger modules</p>
  </section>

  <section class="section col-left" style="top:403px">
    <h2 class="section-title">Human Resources</h2>
    <p class="section-intro">With our online HR tools, you can empower yourself to take control of your human resource needs or let us do it.</p>
    <p class="feature"><strong>Get Big Company Services</strong> - By using our online tools in conjunction with your service team, you will have access to HR services only afforded by some of the largest companies.</p>
    <p class="feature"><strong>Library</strong> -&nbsp; Our online document library lets you and employees create your own library of information accessible at any time. Employees can upload documents and forms that can be kept in history as long as needed.</p>
  </section>

  <section class="section col-left" style="top:601px">
    <h2 class="section-title">Benefit Enrollment</h2>
    <p class="feature"><strong>Easy and Quick Enrollment</strong> - our intuitive user experience quickly walks employees through their benefit enrollment process and allows them to compare different plans and select those that best meet their life needs.</p>
    <p class="feature"><strong>Flexible Benefit Plans and Easy Setup Options</strong> - Offer your clients Fortune 500 benefit plans or administer their plans in an easy to use, yet flexible benefit administration module.</p>
    <p class="feature"><strong>You Pick</strong> - With our flexible contribution MTsetup features, you can contribute in any manner to your employees’ benefits while the system automatically</p>
  </section>

  <section class="section col-right" style="top:65px">
    <h2 class="section-title">On-boarding</h2>
    <p class="feature"><strong>Customize your Onb-oarding</strong> – you can customize your<br>on boarding experience to your hiring needs as well as provide<br>multiple workflows for different employee types. The on boarding<br>experience can be branded for you, providing a personalized experience<br>for the employees.</p>
    <p class="feature"><strong>Custom Document Management</strong> – our custom document mapping feature lets you use your own forms and documents as part of the on boarding and hiring process. When these forms are completed – and electronically signed – they stay in history as long as needed.</p>
    <p class="feature"><strong>Intuitive</strong> – with a focus on the user experience, your employees will find it easy and quick to get on boarded with you</p>
  </section>

  <section class="section col-right" style="top:291px">
    <h2 class="section-title">Applicant Tracking</h2>
    <p class="feature"><strong>Create and Post Jobs</strong> - you can create jobs with just a few clicks Right and Hire the post them on all the popular job sites</p>
    <p class="feature"><strong>People</strong> -&nbsp; by posting on popular job boards, as well as a proprietary database of job seekers, you will reach more candidates.&nbsp; You can choose to receive profiles of candidates that only match your background and specifications.</p>
    <p class="feature"><strong>Manage the Hiring Process</strong> - review candidates via video or online conferencing, review voice interviews, schedule in person interviews, have candidates answer certain online questions, and manage this entire process to find the right people. Once hired, they can be on boarded automatically.</p>
  </section>

  <section class="section col-right" style="top:488px">
    <h2 class="section-title">Time and Attendance</h2>
    <p class="section-intro">Make Time Entry Easy - Simplify time tracking so you can spend less time on payroll tasks.</p>
    <p class="feature"><strong>Everywhere Access</strong> - Web interface, mobile apps, and on-premise time clocks allow employees to log their time wherever they are.</p>
    <p class="feature"><strong>Plug and Play Time Clocks</strong> – Time clocks are delivered ready-to-use with little or no setup required.</p>
  </section>

  <section class="section col-right" style="top:643px">
    <h2 class="section-title">ACA Compliance</h2>
    <p class="feature"><strong>Client Tools</strong> - Provide you with reporting and analysis tools online so you can monitor ACA information and be proactive in managing your needs.</p>
    <p class="feature"><strong>Affordability Test</strong> - Provide your company with information about plan affordability with your employees so your company can stay in compliance.</p>
    <p class="feature"><strong>Large Employer Analysis</strong> - Analyze your&nbsp; control groups to determine if you will fall under the rules of ACA for large employer groups.</p>
  </section>
</div>
</body>
</html>
```